Software manual (User manual)

We need a manual for our online e-learning software. Basically what we're looking for is an Adobe InDesign setup (file) where we can add new pages and adjust textual content ourselves.

So the designer would have to come up with an elegant frontpage, page 2,3,4,5 with textual content (some lorem ipsum placeholder text) in a nice setup and a backpage.

We would like the manual to be presented in purple, specifically the purple being used in our logo (maybe cover the enitre front and backpage in purple) which is our main color (together with grey), at least for front- and back-page.

The design should be simple and elegant. Myriad-Pro Light is the font we'd like to see in headings while maybe something like Helvetica being used for the bulk text.

Industry/Entity Type

Software

Requirements
Must have
• The manual must have our logo in either colors or white depending on your choice of setup. See attached colored logo. We accept changing logo colors to all white.

It should include our email on the backpage together with the company name.

The text "User manual" should be present on the frontpage.

Either the front or backpage should have the text "edition" or "version" with a number or something similar so it's easier for users to distinguish the old manuals from the new ones.

The size should be A4

Should include an index, preferbly set up so that is updates automatically if pages are added/removed.

Each page should be numbered, aside from front and back.

As this is a user manual we do not want images. Vector graphics are ok.

"Less is more"

```html
<!DOCTYPE html>
<html lang="en">
<head>
<meta charset="utf-8">
<title>Studyo User Manual – Spread</title>
<link rel="stylesheet" href="https://fonts.googleapis.com/css2?family=Source+Sans+3:wght@300;400;700&family=Arimo:wght@400&display=swap">
<style>
  :root{
    --purple:#6b2c82;
    --grey:#58585a;
    --grey-light:#8a8a8c;
    --rule:#dcdcdc;
    --paper:#ffffff;
  }
  *{margin:0;padding:0;box-sizing:border-box}
  html,body{width:1200px;height:283px;overflow:hidden;background:var(--paper)}
  .spread{position:relative;width:1200px;height:283px}
  .page{position:absolute;top:0;width:200px;height:283px;border-right:1px solid var(--rule);overflow:hidden;background:var(--paper)}
  .brand{position:absolute;font-family:"Source Sans 3",sans-serif;font-weight:700;color:var(--purple);letter-spacing:-.2px;line-height:1}
  .brand--small{font-size:13px}
  .brand--large{font-size:18px}
  .email{position:absolute;font-family:"Arimo",sans-serif;font-size:3.6px;color:var(--grey)}
  .version{position:absolute;top:26px;right:24px;font-family:"Source Sans 3",sans-serif;font-weight:300;font-size:8px;color:var(--grey)}
  .contents-title{position:absolute;top:98px;left:32px;font-family:"Source Sans 3",sans-serif;font-weight:300;font-size:8px;color:var(--grey)}
  .toc{position:absolute;top:147px;left:30px;width:150px;list-style:none;font-family:"Arimo",sans-serif;font-size:5px;line-height:6.2px;color:var(--grey)}
  .toc li{display:grid;grid-template-columns:75px 10px 1fr}
  .toc .entry{text-align:center}
  .manual-title{position:absolute;top:244px;left:15px;font-family:"Source Sans 3",sans-serif;font-weight:700;font-size:15px;color:var(--purple)}
  .col{position:absolute;width:56px;overflow:hidden;font-family:"Arimo",sans-serif;font-size:4px;line-height:4.9px;color:var(--grey);text-align:left}
  .col p{margin-bottom:2px}
  .placeholder{position:absolute;background:linear-gradient(160deg,#f1eef3,#dcd6e0);border-radius:2px}
  .folio{position:absolute;bottom:9px;font-family:"Arimo",sans-serif;font-size:4.5px;color:var(--grey)}
</style>
</head>
<body>
<div class="spread">

  <!-- Back cover -->
  <section class="page back-cover" style="left:0">
    <div class="brand brand--large" style="left:20px;top:228px">Studyo</div>
    <div class="email" style="left:28px;top:254px">email: info@studyo.example</div>
  </section>

  <!-- Front cover -->
  <section class="page front-cover" style="left:200px">
    <div class="version">Version iiv</div>
    <h2 class="contents-title">Contents</h2>
    <ol class="toc">
      <li><span>1</span><span>-</span><span class="entry">Ure modiamcore</span></li>
      <li><span>2</span><span>-</span><span class="entry">Core vendion secten</span></li>
      <li><span>3</span><span>-</span><span class="entry">Vullaorcinci</span></li>
      <li><span>4</span><span>-</span><span class="entry">Blam, verat, conse</span></li>
      <li><span>5</span><span>-</span><span class="entry">Facil iuscincin hendih</span></li>
      <li><span>6</span><span>-</span><span class="entry">Exeros nullaorper</span></li>
      <li><span>7</span><span>-</span><span class="entry">Se volesed</span></li>
      <li><span>8</span><span>-</span><span class="entry">Doloborte dignibh</span></li>
      <li><span>9</span><span>-</span><span class="entry">Exeros nim dolut accum</span></li>
      <li><span>10</span><span>-</span><span class="entry">VeroTat lutat.</span></li>
    </ol>
    <div class="brand brand--large" style="left:15px;top:222px">Studyo</div>
    <h1 class="manual-title">User Manual</h1>
  </section>

  <!-- Page 2 -->
  <section class="page" style="left:400px">
    <div class="col" style="left:6px;top:8px;height:255px"><p>Tae ea adis et aut magnatio vitae in ipsam voles quas magna lorem nam facing rerum adip eumque dolorum nobis sit utquiat volupta dolore ullam quiatur modit harum ipsum vero veles exerum quis volo consequat amet porro aut faccum sequi nonsedit et ute dolupta rerum sitatur mint reprovit quamus sed erum.</p><p>Tae ea adis et aut magnatio vitae in ipsam voles quas magna lorem nam facing rerum adip eumque dolorum nobis sit utquiat volupta dolore ullam quiatur modit harum ipsum vero veles exerum quis volo consequat amet porro aut faccum sequi nonsedit et ute dolupta rerum sitatur mint reprovit quamus sed erum.</p></div>
    <div class="col" style="left:70px;top:8px;height:118px"><p>Tae ea adis et aut magnatio vitae in ipsam voles quas magna lorem nam facing rerum adip eumque dolorum nobis sit utquiat volupta dolore ullam quiatur modit harum ipsum vero veles exerum quis volo consequat amet porro aut faccum sequi nonsedit et ute dolupta rerum sitatur mint reprovit quamus sed erum.</p><p>Tae ea adis et aut magnatio vitae in ipsam voles quas magna lorem nam facing rerum adip eumque dolorum nobis sit utquiat volupta dolore ullam quiatur modit harum ipsum vero veles exerum quis volo consequat amet porro aut faccum sequi nonsedit et ute dolupta rerum sitatur mint reprovit quamus sed erum.</p></div>
    <div class="placeholder" role="img" aria-label="Line drawing of an open laptop" style="left:72px;top:132px;width:62px;height:52px"></div>
    <div class="col" style="left:70px;top:190px;height:70px"><p>Tae ea adis et aut magnatio vitae in ipsam voles quas magna lorem nam facing rerum adip eumque dolorum nobis sit utquiat volupta dolore ullam quiatur modit harum ipsum vero veles exerum quis volo consequat amet porro aut faccum sequi nonsedit et ute dolupta rerum sitatur mint reprovit quamus sed erum.</p><p>Tae ea adis et aut magnatio vitae in ipsam voles quas magna lorem nam facing rerum adip eumque dolorum nobis sit utquiat volupta dolore ullam quiatur modit harum ipsum vero veles exerum quis volo consequat amet porro aut faccum sequi nonsedit et ute dolupta rerum sitatur mint reprovit quamus sed erum.</p></div>
    <div class="col" style="left:138px;top:8px;height:255px"><p>Tae ea adis et aut magnatio vitae in ipsam voles quas magna lorem nam facing rerum adip eumque dolorum nobis sit utquiat volupta dolore ullam quiatur modit harum ipsum vero veles exerum quis volo consequat amet porro aut faccum sequi nonsedit et ute dolupta rerum sitatur mint reprovit quamus sed erum.</p><p>Tae ea adis et aut magnatio vitae in ipsam voles quas magna lorem nam facing rerum adip eumque dolorum nobis sit utquiat volupta dolore ullam quiatur modit harum ipsum vero veles exerum quis volo consequat amet porro aut faccum sequi nonsedit et ute dolupta rerum sitatur mint reprovit quamus sed erum.</p></div>
    <div class="folio" style="left:6px">2</div>
  </section>

  <!-- Page 3 -->
  <section class="page" style="left:600px">
    <div class="brand brand--small" style="left:14px;top:26px">Studyo</div>
    <div class="col" style="left:14px;top:98px;height:165px"><p>Tae ea adis et aut magnatio vitae in ipsam voles quas magna lorem nam facing rerum adip eumque dolorum nobis sit utquiat volupta dolore ullam quiatur modit harum ipsum vero veles exerum quis volo consequat amet porro aut faccum sequi nonsedit et ute dolupta rerum sitatur mint reprovit quamus sed erum.</p><p>Tae ea adis et aut magnatio vitae in ipsam voles quas magna lorem nam facing rerum adip eumque dolorum nobis sit utquiat volupta dolore ullam quiatur modit harum ipsum vero veles exerum quis volo consequat amet porro aut faccum sequi nonsedit et ute dolupta rerum sitatur mint reprovit quamus sed erum.</p></div>
    <div class="col" style="left:76px;top:98px;height:165px"><p>Tae ea adis et aut magnatio vitae in ipsam voles quas magna lorem nam facing rerum adip eumque dolorum nobis sit utquiat volupta dolore ullam quiatur modit harum ipsum vero veles exerum quis volo consequat amet porro aut faccum sequi nonsedit et ute dolupta rerum sitatur mint reprovit quamus sed erum.</p><p>Tae ea adis et aut magnatio vitae in ipsam voles quas magna lorem nam facing rerum adip eumque dolorum nobis sit utquiat volupta dolore ullam quiatur modit harum ipsum vero veles exerum quis volo consequat amet porro aut faccum sequi nonsedit et ute dolupta rerum sitatur mint reprovit quamus sed erum.</p></div>
    <div class="col" style="left:138px;top:98px;height:165px"><p>Tae ea adis et aut magnatio vitae in ipsam voles quas magna lorem nam facing rerum adip eumque dolorum nobis sit utquiat volupta dolore ullam quiatur modit harum ipsum vero veles exerum quis volo consequat amet porro aut faccum sequi nonsedit et ute dolupta rerum sitatur mint reprovit quamus sed erum.</p><p>Tae ea adis et aut magnatio vitae in ipsam voles quas magna lorem nam facing rerum adip eumque dolorum nobis sit utquiat volupta dolore ullam quiatur modit harum ipsum vero veles exerum quis volo consequat amet porro aut faccum sequi nonsedit et ute dolupta rerum sitatur mint reprovit quamus sed erum.</p></div>
    <div class="folio" style="right:6px">3</div>
  </section>

  <!-- Page 4 -->
  <section class="page" style="left:800px">
    <div class="brand brand--small" style="left:14px;top:26px">Studyo</div>
    <div class="col" style="left:14px;top:98px;height:165px"><p>Tae ea adis et aut magnatio vitae in ipsam voles quas magna lorem nam facing rerum adip eumque dolorum nobis sit utquiat volupta dolore ullam quiatur modit harum ipsum vero veles exerum quis volo consequat amet porro aut faccum sequi nonsedit et ute dolupta rerum sitatur mint reprovit quamus sed erum.</p><p>Tae ea adis et aut magnatio vitae in ipsam voles quas magna lorem nam facing rerum adip eumque dolorum nobis sit utquiat volupta dolore ullam quiatur modit harum ipsum vero veles exerum quis volo consequat amet porro aut faccum sequi nonsedit et ute dolupta rerum sitatur mint reprovit quamus sed erum.</p></div>
    <div class="placeholder" role="img" aria-label="Line drawing of an open laptop" style="left:34px;top:124px;width:44px;height:42px"></div>
    <div class="col" style="left:80px;top:50px;height:213px"><p>Tae ea adis et aut magnatio vitae in ipsam voles quas magna lorem nam facing rerum adip eumque dolorum nobis sit utquiat volupta dolore ullam quiatur modit harum ipsum vero veles exerum quis volo consequat amet porro aut faccum sequi nonsedit et ute dolupta rerum sitatur mint reprovit quamus sed erum.</p><p>Tae ea adis et aut magnatio vitae in ipsam voles quas magna lorem nam facing rerum adip eumque dolorum nobis sit utquiat volupta dolore ullam quiatur modit harum ipsum vero veles exerum quis volo consequat amet porro aut faccum sequi nonsedit et ute dolupta rerum sitatur mint reprovit quamus sed erum.</p></div>
    <div class="col" style="left:138px;top:50px;height:213px"><p>Tae ea adis et aut magnatio vitae in ipsam voles quas magna lorem nam facing rerum adip eumque dolorum nobis sit utquiat volupta dolore ullam quiatur modit harum ipsum vero veles exerum quis volo consequat amet porro aut faccum sequi nonsedit et ute dolupta rerum sitatur mint reprovit quamus sed erum.</p><p>Tae ea adis et aut magnatio vitae in ipsam voles quas magna lorem nam facing rerum adip eumque dolorum nobis sit utquiat volupta dolore ullam quiatur modit harum ipsum vero veles exerum quis volo consequat amet porro aut faccum sequi nonsedit et ute dolupta rerum sitatur mint reprovit quamus sed erum.</p></div>
    <div class="folio" style="left:6px">4</div>
  </section>

  <!-- Page 5 -->
  <section class="page" style="left:1000px;border-right:none">
    <div class="brand brand--small" style="left:130px;top:26px">Studyo</div>
    <div class="col" style="left:10px;top:44px;height:219px"><p>Tae ea adis et aut magnatio vitae in ipsam voles quas magna lorem nam facing rerum adip eumque dolorum nobis sit utquiat volupta dolore ullam quiatur modit harum ipsum vero veles exerum quis volo consequat amet porro aut faccum sequi nonsedit et ute dolupta rerum sitatur mint reprovit quamus sed erum.</p><p>Tae ea adis et aut magnatio vitae in ipsam voles quas magna lorem nam facing rerum adip eumque dolorum nobis sit utquiat volupta dolore ullam quiatur modit harum ipsum vero veles exerum quis volo consequat amet porro aut faccum sequi nonsedit et ute dolupta rerum sitatur mint reprovit quamus sed erum.</p></div>
    <div class="col" style="left:66px;top:44px;height:219px"><p>Tae ea adis et aut magnatio vitae in ipsam voles quas magna lorem nam facing rerum adip eumque dolorum nobis sit utquiat volupta dolore ullam quiatur modit harum ipsum vero veles exerum quis volo consequat amet porro aut faccum sequi nonsedit et ute dolupta rerum sitatur mint reprovit quamus sed erum.</p><p>Tae ea adis et aut magnatio vitae in ipsam voles quas magna lorem nam facing rerum adip eumque dolorum nobis sit utquiat volupta dolore ullam quiatur modit harum ipsum vero veles exerum quis volo consequat amet porro aut faccum sequi nonsedit et ute dolupta rerum sitatur mint reprovit quamus sed erum.</p></div>
    <div class="col" style="left:122px;top:84px;height:179px"><p>Tae ea adis et aut magnatio vitae in ipsam voles quas magna lorem nam facing rerum adip eumque dolorum nobis sit utquiat volupta dolore ullam quiatur modit harum ipsum vero veles exerum quis volo consequat amet porro aut faccum sequi nonsedit et ute dolupta rerum sitatur mint reprovit quamus sed erum.</p><p>Tae ea adis et aut magnatio vitae in ipsam voles quas magna lorem nam facing rerum adip eumque dolorum nobis sit utquiat volupta dolore ullam quiatur modit harum ipsum vero veles exerum quis volo consequat amet porro aut faccum sequi nonsedit et ute dolupta rerum sitatur mint reprovit quamus sed erum.</p></div>
    <div class="folio" style="right:6px">5</div>
  </section>

</div>
</body>
</html>
```